Velvet Marketing needs a new website design

We need a homepage and sub-page design for our new marketing consulting business based in Perth, Western Australia. www.velvetmarketing.com.au

About Us:

Velvet Marketing specialises in providing professional and result orientated marketing advice to small and medium sized business. We focus on client's overall marketing communication mix and analyse their current marketing activities and give advise where to invest their budget in the future.

We also function as marketing freelancers and can put the developed marketing plans and strategies into action.

Colour Suggestions based on newly designed logo:
orange, dark blue, black and white

The final design should reflect strategic solutions, success, trust & knowledge.

Please refer to attached documents:
Wireframe - for an indication of the sections needed on the site
Sitemap - as guidance how the content is arranged/interlinked
Services - overview of our marketing consulting service areas
Logo - use as guideline for colours and style

Industry websites that are different and that we like:

1. http://www.lomativa.com/index.htm
- like the simplicity of this site

2. http://www.quillstonemedia.com/ - like the integration of the services into the header

3. http://www.tarevosa.com/
like the concept of the display of services - can you come up with something for us based on our overview of services

Target Market(s)

Marketing Managers & Business Owners (age 30-50) of small to medium sized businesses in Perth/ Western Australia

Industry/Entity Type

Marketing

Requirements
Must have
• - clean design and customised site
- all elements as specified in the wireframes document (provided a few options but open to suggestions and ideas
- looking for ideas to display our services as per overview page which can be integrated into each page of the website
Should not have
• don’t want a template looking site
please don't just copy our wireframes and make the site too boxy

```html
<!DOCTYPE html>
<html lang="en">
<head>
<meta charset="utf-8">
<title>Velvet Marketing</title>
<link href="https://fonts.googleapis.com/css2?family=Ubuntu:wght@400;500;700&family=Arimo:wght@400;700&family=PT+Serif&display=swap" rel="stylesheet">
<style>
:root{
  --orange:#f58220;
  --orange-dark:#e06c0c;
  --ink:#333;
  --grey:#666;
  --light:#ececec;
  --header-bg:#e6e6e6;
  --footer:#2f3846;
  --footer-text:#d5d9df;
  --blue:#1a7fc4;
}
*{margin:0;padding:0;box-sizing:border-box}
html,body{width:948px;height:1200px;overflow:hidden;background:#fff}
body{position:relative;font-family:Arimo,Arial,sans-serif;color:var(--ink);font-size:9px}
ul{list-style:none}
.abs{position:absolute}

/* top navigation */
.topnav{left:0;top:0;width:948px;height:36px;background:linear-gradient(#fafafa,#e9e9e9);border-bottom:1px solid #d5d5d5}
.topnav ul{display:flex;align-items:center;height:36px;padding-left:80px;font-family:Ubuntu,sans-serif;font-size:11px;color:#555}
.topnav li{margin-right:22px}
.topnav .sep{color:#777}
.topnav .active{background:var(--orange);color:#fff;padding:5px 11px;border:2px solid #fff;box-shadow:0 0 2px #aaa;margin-right:42px}

/* header band */
.hero{left:0;top:37px;width:948px;height:317px;background:linear-gradient(#fafafa,var(--header-bg))}
.brand{left:72px;top:62px;display:flex;align-items:center;gap:10px}
.brand-dot{width:48px;height:48px;border-radius:50%;background:var(--orange)}
.brand-name{font-family:Ubuntu,sans-serif;font-weight:500;font-size:34px;line-height:34px;color:var(--orange);width:180px}
.tagline{left:74px;top:159px;font-family:Ubuntu,sans-serif;font-weight:700;font-size:16px;color:var(--orange)}
.intro{left:74px;top:182px;width:322px;font-size:9.5px;line-height:15px;color:#444;text-align:justify}
.checks{left:75px;top:263px;width:240px;display:grid;grid-template-columns:148px 90px;row-gap:10px;font-family:Ubuntu,sans-serif;font-size:12.5px;color:#666}
.checks li{display:flex;align-items:center;gap:8px}
.checks svg{width:14px;height:14px}

.slider-frame{left:446px;top:53px;width:422px;height:284px;background:#fff;border:1px solid #d0d0d0;padding:4px}
.slider-img{width:100%;height:100%;background:linear-gradient(#0b4f8f,#1a8fd8 70%,#5bc4f0)}
.arrow{width:42px;height:34px;background:linear-gradient(#fff,#ddd);border-radius:6px;box-shadow:0 2px 3px rgba(0,0,0,.3);display:flex;align-items:center;justify-content:center}
.arrow.next{left:437px;top:171px}
.arrow.prev{left:838px;top:171px}

/* services */
.svc{top:384px;width:195px}
.svc h3{display:flex;align-items:center;gap:6px;font-family:Ubuntu,sans-serif;font-weight:500;font-size:15px;color:#666;margin-bottom:16px}
.ring{width:22px;height:22px;border-radius:50%;border:4px solid var(--orange);box-shadow:inset 0 0 0 3px #333}
.svc p{font-size:8.8px;line-height:15px;color:#444;text-align:justify}
.svc ul{font-size:8.8px;line-height:18px;color:#444}
.svc li::before{content:"›";margin:0 8px 0 4px;font-weight:700}
.readmore{top:550px;font-size:9px;font-weight:700;color:var(--orange)}
.divider{left:50px;width:820px;height:1px;background:linear-gradient(90deg,transparent,#ccc,transparent)}

/* news row */
.col-title{display:flex;align-items:center;gap:8px;font-family:"PT Serif",serif;font-size:16px;color:#555}
.col-title b{font-family:Ubuntu,sans-serif;font-weight:700;color:var(--orange);font-size:16px}
.icon-sq{width:26px;height:26px;border-radius:4px}
.list{font-size:8.8px;line-height:15px;color:#444}
.list li{display:flex;gap:6px}
.list li::before{content:"›";color:var(--orange);font-weight:700}
.news li{margin-bottom:14px}
.consult li{margin-bottom:5px}
.vline{width:1px;background:repeating-linear-gradient(#ccc 0 2px,transparent 2px 4px)}
.video{left:626px;top:632px;width:242px;height:177px;border:1px solid #ccc;background:#fff;padding:3px}
.video-img{height:148px;background:radial-gradient(circle at 50% 55%,#9aa0aa,#3c4150 75%)}
.video-bar{height:22px;background:linear-gradient(#f4f4f4,#dcdcdc);display:flex;align-items:center;gap:6px;padding:0 6px;font-size:6px;color:#777}
.video-bar .track{flex:1;height:3px;background:#bbb;border-radius:2px}

/* partner strip */
.partners{left:75px;top:840px;width:795px;height:93px;border-radius:20px;background:linear-gradient(#fff,#efefef);border:1px solid #dedede;display:flex;align-items:center;justify-content:space-around;padding:0 30px}
.badge{border-radius:4px}

/* footer */
.footer{left:0;top:973px;width:948px;height:227px;background:var(--footer);border-top:4px solid var(--orange)}
.f-title{font-family:"PT Serif",serif;font-size:21px;color:#e3e6ea;display:flex;align-items:center;gap:10px}
.f-title span{color:var(--orange)}
.f-icon{width:30px;height:30px;border-radius:50%;background:#8b929d}
.f-list{font-family:Ubuntu,sans-serif;font-size:9.5px;line-height:18px;color:var(--footer-text)}
.f-list li::before{content:"*";color:var(--orange);margin-right:6px}
.contact{left:634px;top:1032px;font-family:Ubuntu,sans-serif;font-size:9.5px;line-height:13px;color:var(--footer-text)}
.contact b{font-weight:500;color:#fff}
.contact a{color:var(--orange);text-decoration:none}
.f-rule{left:60px;top:1150px;width:810px;height:1px;background:#556070}
.bottomnav{left:67px;top:1163px;font-family:Ubuntu,sans-serif;font-size:8.5px;color:#fff;word-spacing:2px}
.copy{left:67px;top:1182px;font-family:Ubuntu,sans-serif;font-size:7.5px;color:#fff}
.social{left:662px;top:1168px;display:flex;gap:8px}
.social span{width:28px;height:28px;border-radius:50%;border:2px solid #fff}
</style>
</head>
<body>

<nav class="abs topnav">
  <ul>
    <li class="active">HOME</li>
    <li>ABOUT US</li>
    <li>SERVICES</li><li class="sep">/</li>
    <li>PROJECTS NETWORK BRANDS</li><li class="sep">/</li>
    <li>PORTFOLIO</li><li class="sep">/</li>
    <li>WORK WITH US</li><li class="sep">/</li>
    <li>EMAIL</li>
  </ul>
</nav>

<header class="abs hero"></header>
<div class="abs brand"><span class="brand-dot"></span><span class="brand-name">Velvet Marketing</span></div>
<h1 class="abs tagline">It all comes down to the Velvet</h1>
<p class="abs intro"><b>At Velvet Marketing, we focus on your overall marketing communication mix</b> and provide marketing solutions that will get you results. As part of our consulting process we provide you with realistic marketing strategies,</p>
<ul class="abs checks">
  <li><svg viewBox="0 0 14 14"><rect x="1" y="2" width="11" height="11" fill="none" stroke="#555" stroke-width="1.6"/><path d="M3 7l3 3 7-9" fill="none" stroke="#333" stroke-width="2"/></svg>Websites</li>
  <li><svg viewBox="0 0 14 14"><rect x="1" y="2" width="11" height="11" fill="none" stroke="#555" stroke-width="1.6"/><path d="M3 7l3 3 7-9" fill="none" stroke="#333" stroke-width="2"/></svg>SEM</li>
  <li><svg viewBox="0 0 14 14"><rect x="1" y="2" width="11" height="11" fill="none" stroke="#555" stroke-width="1.6"/><path d="M3 7l3 3 7-9" fill="none" stroke="#333" stroke-width="2"/></svg>SEO</li>
  <li><svg viewBox="0 0 14 14"><rect x="1" y="2" width="11" height="11" fill="none" stroke="#555" stroke-width="1.6"/><path d="M3 7l3 3 7-9" fill="none" stroke="#333" stroke-width="2"/></svg>Social</li>
  <li><svg viewBox="0 0 14 14"><rect x="1" y="2" width="11" height="11" fill="none" stroke="#555" stroke-width="1.6"/><path d="M3 7l3 3 7-9" fill="none" stroke="#333" stroke-width="2"/></svg>Paid Search</li>
  <li><svg viewBox="0 0 14 14"><rect x="1" y="2" width="11" height="11" fill="none" stroke="#555" stroke-width="1.6"/><path d="M3 7l3 3 7-9" fill="none" stroke="#333" stroke-width="2"/></svg>Media</li>
</ul>

<div class="abs slider-frame"><div class="slider-img" role="img" aria-label="Slide photo: a businesswoman touching a blue digital interface with marketing keywords"></div></div>
<div class="abs arrow next"><svg width="12" height="14" viewBox="0 0 12 14"><path d="M2 1l8 6-8 6z" fill="#222"/></svg></div>
<div class="abs arrow prev"><svg width="12" height="14" viewBox="0 0 12 14"><path d="M10 1L2 7l8 6z" fill="#222"/></svg></div>

<div class="abs divider" style="top:358px"></div>

<section class="abs svc" style="left:72px">
  <h3><span class="ring"></span>Online Marketing</h3>
  <ul>
    <li>Small business website design</li>
    <li>Company logo design</li>
    <li>Domains and web hosting</li>
    <li>Cheapest web design offer</li>
    <li>Some recent client websites</li>
  </ul>
</section>
<section class="abs svc" style="left:277px">
  <h3><span class="ring"></span>Brand Marketing</h3>
  <p><b>Branding is an important part of your business recognition</b> and this can be achieved through a wide range of marketing services from printand this can be achieved through a wide</p>
  <ul style="margin-top:4px">
    <li>Cheapest web design offer</li>
    <li>Some recent client websites</li>
  </ul>
</section>
<section class="abs svc" style="left:482px;width:184px">
  <h3><span class="ring"></span>Event Management</h3>
  <p><b>Events are an effective way to increase your brand</b> exposure to potential customers but can also be used to increase staff motivation and strengthening the organisational culture of your business.culture of your business.culture of your business.</p>
</section>
<section class="abs svc" style="left:688px;width:184px">
  <h3><span class="ring"></span>Print Marketing</h3>
  <p><b>Events are an effective way to increase your brand</b> exposure to potential customers but can also be used to increase staff motivation and strengthening the organisational culture of your business. increase</p>
</section>
<span class="abs readmore" style="left:191px">Readmore [+]</span>
<span class="abs readmore" style="left:404px">Readmore [+]</span>
<span class="abs readmore" style="left:611px">Readmore [+]</span>
<span class="abs readmore" style="left:818px">Readmore [+]</span>

<div class="abs divider" style="top:580px"></div>

<div class="abs col-title" style="left:88px;top:600px"><span class="icon-sq" style="background:var(--orange)"></span>Latest <b>NEWS</b></div>
<ul class="abs list news" style="left:75px;top:641px;width:218px">
  <li>Social Design Strategy: Working from the Outside In Insights on what social</li>
  <li>Medialoft Buys Adpoint, Bolsters Cross-Media Buying Tools Company</li>
  <li>Bayport Star Gives Chirper Advice to League Draftees Rovers running</li>
  <li>Bayport Star Gives Chirper</li>
</ul>
<div class="abs vline" style="left:306px;top:632px;height:170px"></div>

<div class="abs col-title" style="left:318px;top:600px"><span class="icon-sq" style="background:var(--blue);border-radius:50%"></span>Internet Marketing <b>CONSULTING</b></div>
<ul class="abs list consult" style="left:322px;top:643px;width:275px">
  <li>Should I embrace social networking for my marketing plans?</li>
  <li>Would we benefit from putting videos online?</li>
  <li>How does my site traffic and usage compare to the competi</li>
  <li>What are microsites and should they be used?</li>
  <li>Can you provide us with benchmarks to measure and track</li>
  <li>We're in a very competitive market and I need to find ways to</li>
  <li>How does my site traffic and usage compare to the competi</li>
  <li>What are microsites and should they be used?</li>
</ul>
<div class="abs vline" style="left:612px;top:632px;height:170px"></div>

<div class="abs col-title" style="left:626px;top:598px"><span class="icon-sq" style="background:#8a8f98;border-radius:50%"></span>Latest <b>VIDEOS</b></div>
<div class="abs video">
  <div class="video-img" role="img" aria-label="Video still: metallic balls on a grey surface with the words online marketing"></div>
  <div class="video-bar">
    <svg width="6" height="7"><rect width="2" height="7" fill="#777"/><rect x="4" width="2" height="7" fill="#777"/></svg>
    <span class="track"></span>
    <span>0:46</span>
  </div>
</div>

<div class="abs partners">
  <span class="badge" style="width:66px;height:66px;background:var(--orange);border:3px solid #fff;box-shadow:0 0 3px #aaa"></span>
  <span class="badge" style="width:140px;height:44px;background:#d9d9d9"></span>
  <span class="badge" style="width:82px;height:52px;background:linear-gradient(#fff 55%,var(--orange) 55%);border:1px solid #ccc"></span>
  <span class="badge" style="width:140px;height:44px;background:#d9d9d9"></span>
  <span class="badge" style="width:82px;height:52px;background:linear-gradient(#fff 55%,var(--orange) 55%);border:1px solid #ccc"></span>
</div>

<footer class="abs footer"></footer>
<div class="abs f-title" style="left:74px;top:986px"><span class="f-icon"></span>Our <span>Services</span></div>
<ul class="abs f-list" style="left:78px;top:1032px">
  <li>Web Design / Development</li><li>Ecommerce Web Development</li><li>Search Engine Optimization</li><li>Link Building Services</li><li>SEO Copywriting</li>
</ul>
<ul class="abs f-list" style="left:258px;top:1033px">
  <li>Web Design / Development</li><li>Ecommerce Web Development</li><li>Link Building Services</li><li>SEO Copywriting</li>
</ul>
<ul class="abs f-list" style="left:430px;top:1032px">
  <li>Web Design / Development</li><li>Ecommerce Web Development</li><li>Search Engine Optimization</li><li>Link Building Services</li><li>SEO Copywriting</li>
</ul>
<div class="abs f-title" style="left:620px;top:986px"><span class="f-icon"></span>Contact <span>Us @</span></div>
<div class="abs contact">
  <b>HEAD OFFICE:</b> Velvet Marketing<br>Harlow Bay (Perth)<br>Western Australia 6110<br><br>
  <b>PHONE:</b> 0400 555 218<br>email: <a>info@velvetmarketing.com.au</a><br><br>Send Email using the Online Form
</div>
<div class="abs f-rule"></div>
<div class="abs bottomnav">HOME &nbsp;/ &nbsp;ABOUT US &nbsp;/ &nbsp;SERVICES &nbsp;/ &nbsp;PROJECTS/ NETWORK/ BRANDS &nbsp;/ &nbsp;MAINDIV &nbsp;/ &nbsp;WORK WITH US &nbsp;/ &nbsp;EMAIL</div>
<div class="abs copy">© COPYRIGHT © 2012 · LUMEN THEME FRAMEWORK BY NORTHPRESS · SITEPRESS · LOG IN</div>
<div class="abs social">
  <span style="background:#3b5e9c"></span><span style="background:#2aa0d8"></span><span style="background:#f08a24"></span><span style="background:#d23a2e"></span>
</div>

</body>
</html>
```